National Virtual accounting firm needs website designed

I need a wordpress website design for a national virtual accounting firm. I will upload my business card, logo, and postcards that I have had designed and followed the same style. I want a similar style to be followed so I can keep the running theme similar.

Services include:

Tax Services:
Tax preparation and planning services for Individuals, businesses, estates, and nonprofits
Full Service Payroll for Businesses
QVT Audit Representation

Consulting:
Entity Selection & Restructuring
Financial Projections & Forecasts
Retirement Planning
IPO Readiness

Accounting:
Bookkeeping
Reviews and Compilations
Payroll Services

Other Services:
CFO Services
Compliance Services
Controller Services
Software Implementations for Tenvolk, Brombalt, and Plovena.

Target Market(s)

small to medium size businesses, and individuals

Industry/Entity Type

accounting firms

Font styles to use
Sans Serif

Colors
59FF00
82FF00
B8FF75
E3FFCB
F4FFEA

Requirements
Must have
• Color schematics from the logo and post cards/business cards

```html
<!DOCTYPE html>
<html lang="en">
<head>
<meta charset="utf-8">
<title>Verdano – Virtual Accounting</title>
<link rel="stylesheet" href="https://fonts.googleapis.com/css2?family=Montserrat:wght@400;500;600;700&display=swap">
<style>
:root{
  --green:#4fb848;
  --green-dark:#3e9e38;
  --green-pale:#e2f6da;
  --green-tab:#c4f7b0;
  --green-card:#dff7d5;
  --yellow:#ffc600;
  --cream:#fdf8ec;
  --navy:#1c3556;
  --ink:#1d1d1d;
  --muted:#5a5a5a;
  --footer:#141414;
  --white:#ffffff;
}
*{box-sizing:border-box;margin:0;padding:0}
html,body{width:1200px;height:5013px;overflow:hidden}
body{font-family:'Montserrat',sans-serif;color:var(--ink);background:var(--white);position:relative}
.abs{position:absolute}
a{color:inherit;text-decoration:none}

/* header */
.site-header{position:absolute;left:0;top:0;width:1200px;height:84px;background:var(--cream)}
.brand{position:absolute;left:108px;top:22px;display:flex;align-items:center;gap:10px;font-size:34px;font-weight:500;letter-spacing:1px;color:var(--ink)}
.brand-dot{width:22px;height:22px;border-radius:50%;background:var(--yellow)}
.main-nav{position:absolute;left:422px;top:31px;display:flex;gap:0;font-size:14.5px;font-weight:600}
.main-nav a{margin-right:22px}

/* hero */
.hero{position:absolute;left:0;top:84px;width:1200px;height:610px;background:linear-gradient(110deg,#3b4d66 0%,#22375a 45%,#2b4a78 70%,#33445e 100%)}
.hero-title{position:absolute;left:113px;top:148px;font-size:50px;font-weight:700;line-height:52px;color:var(--white)}
.btn{display:inline-block;background:var(--green);color:var(--white);font-weight:600;border-radius:24px;text-align:center}
.hero .btn{position:absolute;left:113px;top:283px;width:136px;height:36px;line-height:36px;font-size:14px}
.hero-curve{position:absolute;left:0;top:600px}

/* about */
.about-photo{position:absolute;left:157px;top:737px;width:386px;height:386px;border-radius:50%;border:6px solid var(--yellow);background:radial-gradient(circle at 40% 40%,#4a86b8,#16385e 70%)}
.about h2{position:absolute;left:600px;top:778px;font-size:33px;font-weight:700}
.about p{position:absolute;left:602px;top:840px;width:400px;font-size:12.6px;line-height:27.4px;color:var(--muted)}
.about .btn{position:absolute;left:602px;top:1063px;width:135px;height:42px;line-height:42px;font-size:14px}

/* services */
.services-bg{position:absolute;left:0;top:1190px;width:1200px;height:1665px}
.section-title{position:absolute;left:0;width:1200px;text-align:center;font-size:33px;font-weight:700}
.tab{position:absolute;top:1370px;width:220px;height:103px;line-height:103px;text-align:center;font-size:19px;font-weight:700;background:var(--green-tab);color:var(--ink)}
.tab.active{background:var(--green);color:var(--white)}
.tab-panel{position:absolute;left:113px;top:1474px;width:977px;height:1262px;border:2px solid var(--green)}
.svc-box{position:absolute;padding:52px 26px 0 26px}
.svc-box h3{font-size:21px;font-weight:700;line-height:29px;letter-spacing:-0.3px;margin-bottom:12px}
.svc-box p{font-size:12.6px;line-height:27.4px}
.svc-box .more{display:block;margin-top:8px;font-size:14px;font-weight:700}
.svc-yellow{background:var(--yellow);color:var(--ink)}
.svc-yellow h3,.svc-yellow p{max-width:470px}
.svc-yellow p{max-width:420px}
.svc-green{background:var(--green);color:var(--white)}
.svc-photo{position:absolute;width:463px;height:266px}

/* why */
.why-card{position:absolute;top:3040px;width:297px;height:235px;background:var(--green-card);box-shadow:0 4px 10px rgba(0,0,0,.12);text-align:center}
.why-card svg{position:absolute;left:113px;top:40px}
.why-card h3{position:absolute;left:0;top:162px;width:100%;font-size:22px;font-weight:700}

/* testimonials */
.testi-bg{position:absolute;left:0;top:3390px;width:1200px;height:660px;background:var(--green-pale)}
.testi-card{position:absolute;top:3545px;width:295px;height:400px;background:var(--white);overflow:hidden;box-shadow:0 2px 8px rgba(0,0,0,.08)}
.testi-card .quote{position:absolute;left:14px;top:14px}
.testi-card p{position:absolute;left:20px;top:62px;width:255px;text-align:center;font-size:12.6px;line-height:25.5px;color:var(--muted)}
.testi-card .wave{position:absolute;left:0;top:232px}
.testi-card .avatar{position:absolute;left:100px;top:190px;width:95px;height:95px;border-radius:50%;border:4px solid var(--white);background:radial-gradient(circle at 50% 40%,#c9d3dc,#7c8da0)}
.testi-card h4{position:absolute;left:0;top:315px;width:100%;text-align:center;font-size:23px;font-weight:700;color:var(--white)}
.testi-card small{position:absolute;left:0;top:350px;width:100%;text-align:center;font-size:13px;color:var(--white)}
.arrow{position:absolute;top:3713px;width:44px;height:44px;border-radius:50%}

/* contact */
.contact-bg{position:absolute;left:0;top:4050px;width:1200px;height:590px;background:linear-gradient(180deg,#f4fbf1,#ffffff)}
.info-item{position:absolute;left:122px;display:flex;gap:12px}
.info-icon{width:42px;height:42px;border-radius:50%;border:2px solid var(--green);display:flex;align-items:center;justify-content:center;flex:none}
.info-item h5{font-size:14px;font-weight:700;margin-top:2px}
.info-item span{display:block;font-size:12.6px;line-height:26px;color:var(--muted)}
.field{position:absolute;background:var(--white);border:1px solid #e3e3e3;border-radius:6px;font-size:12px;color:#777;padding:14px 16px}
.submit{position:absolute;left:517px;top:4490px;width:138px;height:43px;line-height:43px;font-size:15px}

/* footer */
.site-footer{position:absolute;left:0;top:4640px;width:1200px;height:373px;background:var(--footer);color:var(--white)}
.site-footer .brand{left:90px;top:92px;color:var(--white)}
.social{position:absolute;top:184px;display:flex;gap:22px;left:116px}
.social span{width:30px;height:30px;border:2px solid var(--white);border-radius:50%}
.foot-col{position:absolute;top:100px}
.foot-col h4{font-size:23px;font-weight:700;line-height:30px;margin-bottom:12px}
.foot-col li{list-style:none;font-size:13px;line-height:27.5px}
.newsletter{position:absolute;left:853px;top:180px;width:258px;height:42px;border-radius:22px;background:var(--white);font-size:12.6px;color:#888;padding:13px 12px}
.newsletter i{position:absolute;right:0;top:0;width:64px;height:42px;border-radius:22px;background:var(--green)}
.foot-rule{position:absolute;left:115px;top:325px;width:970px;height:1px;background:#555}
.copyright{position:absolute;left:0;top:338px;width:1200px;text-align:center;font-size:12.5px;font-weight:600}
</style>
</head>
<body>

<header class="site-header">
  <div class="brand"><span class="brand-dot"></span>VERDANO</div>
  <nav class="main-nav">
    <a>Home</a><a>About Us</a><a style="margin-right:31px">Our Services</a><a>Why Choose Us</a><a style="margin-right:27px">Testimonials</a><a>Contact us</a>
  </nav>
</header>

<section class="hero" role="img" aria-label="Hands at a laptop overlaid with glowing hexagon business icons">
  <h1 class="hero-title">Welcome To<br>Verdano</h1>
  <a class="btn">Get Started</a>
</section>
<svg class="hero-curve" width="1200" height="100" viewBox="0 0 1200 100">
  <path d="M0 78 Q600 -10 1200 88 L1200 100 L0 100Z" fill="#ffffff"/>
  <path d="M0 78 Q600 -10 1200 88 L1200 80 Q600 -22 0 68Z" fill="#4fb848"/>
</svg>

<section class="about">
  <div class="about-photo" role="img" aria-label="Hands typing on a laptop with financial dashboards on screen"></div>
  <h2>About Us</h2>
  <p>Lorem Ipsum is simply dummy text of the printing and typesetting industry. Lorem Ipsum has been the industry's standard dummy text ever since the 1500s, when an unknown printer took a galley of type and scrambled it to make a type specimen book. It has survived not only five centuries, but also the leap into electronic typesetting, remaining essentially</p>
  <a class="btn">Read More</a>
</section>

<svg class="services-bg" viewBox="0 0 1200 1665" preserveAspectRatio="none">
  <path d="M0 110 Q600 -60 1200 110 L1200 1665 L0 1665Z" fill="#e2f6da"/>
</svg>
<h2 class="section-title" style="top:1296px">Our Services</h2>
<div class="tab active" style="left:113px">Tax Services</div>
<div class="tab" style="left:365px">Consulting</div>
<div class="tab" style="left:618px">Accounting</div>
<div class="tab" style="left:868px">Other Services</div>
<div class="tab-panel"></div>

<div class="svc-box svc-yellow" style="left:115px;top:1587px;width:578px;height:290px;padding-top:50px">
  <h3>Tax preparation and planning services for Individuals, businesses, estates, and nonprofits</h3>
  <p>Lorem Ipsum is simply dummy text of the printing and typesetting industry. Lorem Ipsum has been the industry's</p>
  <span class="more">Read More..</span>
</div>
<div class="svc-photo" role="img" aria-label="Colleagues meeting around a table with laptops" style="left:615px;top:1531px;background:linear-gradient(135deg,#d7d2c8,#8a7a66)"></div>

<div class="svc-photo" role="img" aria-label="Presenter at a flip chart addressing a team" style="left:124px;top:1940px;background:linear-gradient(135deg,#e8e6e0,#6f6a62)"></div>
<div class="svc-box svc-green" style="left:507px;top:1997px;width:571px;height:288px;padding:36px 20px 0 97px">
  <h3>Full Service Payroll for Businesses</h3>
  <p>Lorem Ipsum is simply dummy text of the printing and typesetting industry. Lorem Ipsum has been the industry's standard dummy text ever since the 1500s, when an unknown printer took a galley of type and scrambled it to make a type</p>
  <span class="more">Read More..</span>
</div>

<div class="svc-box svc-yellow" style="left:115px;top:2407px;width:578px;height:290px;padding-top:48px">
  <h3>QVT Audit Representation</h3>
  <p>Lorem Ipsum is simply dummy text of the printing and typesetting industry. Lorem Ipsum has been the industry's standard dummy text ever since the 1500s, when an unknown printer took a galley of type and scrambled it to make a type</p>
  <span class="more">Read More..</span>
</div>
<div class="svc-photo" role="img" aria-label="Two colleagues reviewing documents in an office" style="left:615px;top:2350px;background:linear-gradient(135deg,#eeeae4,#a88f74)"></div>

<h2 class="section-title" style="top:2953px">Why Choose Us?</h2>
<div class="why-card" style="left:113px">
  <svg width="72" height="100" viewBox="0 0 72 100" aria-hidden="true">
    <circle cx="30" cy="42" r="12" fill="#4fb848"/><path d="M8 88 Q8 60 30 60 Q52 60 52 88Z" fill="#4fb848"/>
    <circle cx="54" cy="80" r="14" fill="#4fb848" stroke="#dff7d5" stroke-width="3"/><path d="M47 80 L52 85 L61 75" stroke="#fff" stroke-width="3" fill="none"/>
    <path d="M36 4 L39 12 L47 12 L41 17 L43 25 L36 20 L29 25 L31 17 L25 12 L33 12Z" fill="#4fb848"/>
  </svg>
  <h3>Experienced</h3>
</div>
<div class="why-card" style="left:453px">
  <svg width="72" height="100" viewBox="0 0 72 100" aria-hidden="true">
    <circle cx="36" cy="46" r="12" fill="#4fb848"/><path d="M14 96 Q14 64 36 64 Q58 64 58 96Z" fill="#4fb848"/>
    <rect x="26" y="6" width="20" height="14" rx="3" fill="#4fb848"/><circle cx="8" cy="24" r="7" fill="#4fb848"/><circle cx="64" cy="24" r="7" fill="#4fb848"/>
  </svg>
  <h3>Professional</h3>
</div>
<div class="why-card" style="left:793px">
  <svg width="72" height="100" viewBox="0 0 72 100" aria-hidden="true">
    <circle cx="40" cy="26" r="18" fill="none" stroke="#4fb848" stroke-width="4"/><text x="40" y="34" text-anchor="middle" font-size="22" font-weight="700" fill="#4fb848" font-family="Montserrat,sans-serif">$</text>
    <path d="M0 70 L22 70 Q32 62 44 70 L60 66 Q68 66 62 74 L40 86 L0 86Z" fill="#4fb848"/>
  </svg>
  <h3>Affordable</h3>
</div>

<div class="testi-bg"></div>
<h2 class="section-title" style="top:3476px">Testimonials</h2>

<div class="testi-card" style="left:110px">
  <svg class="quote" width="40" height="30" viewBox="0 0 40 30" aria-hidden="true"><path d="M2 28 V16 Q2 4 14 2 V8 Q8 10 8 14 H16 V28Z M22 28 V16 Q22 4 34 2 V8 Q28 10 28 14 H36 V28Z" fill="#ffc600"/></svg>
  <p>Lorem Ipsum is simply dummy text of the printing and typesetting industry. Lorem Ipsum has been the industry's standard dummy text ever</p>
  <svg class="wave" width="295" height="170" viewBox="0 0 295 170" aria-hidden="true"><path d="M0 30 Q147 -20 295 30 V170 H0Z" fill="#4fb848"/></svg>
  <div class="avatar" role="img" aria-label="Portrait of client Harlowe"></div>
  <h4>Harlowe</h4><small>Client</small>
</div>
<div class="testi-card" style="left:453px">
  <svg class="quote" width="40" height="30" viewBox="0 0 40 30" aria-hidden="true"><path d="M2 28 V16 Q2 4 14 2 V8 Q8 10 8 14 H16 V28Z M22 28 V16 Q22 4 34 2 V8 Q28 10 28 14 H36 V28Z" fill="#ffc600"/></svg>
  <p>Lorem Ipsum is simply dummy text of the printing and typesetting industry. Lorem Ipsum has been the industry's standard dummy text ever</p>
  <svg class="wave" width="295" height="170" viewBox="0 0 295 170" aria-hidden="true"><path d="M0 30 Q147 -20 295 30 V170 H0Z" fill="#4fb848"/></svg>
  <div class="avatar" role="img" aria-label="Portrait of client Delmar"></div>
  <h4>Delmar</h4><small>Client</small>
</div>
<div class="testi-card" style="left:793px">
  <svg class="quote" width="40" height="30" viewBox="0 0 40 30" aria-hidden="true"><path d="M2 28 V16 Q2 4 14 2 V8 Q8 10 8 14 H16 V28Z M22 28 V16 Q22 4 34 2 V8 Q28 10 28 14 H36 V28Z" fill="#ffc600"/></svg>
  <p>Lorem Ipsum is simply dummy text of the printing and typesetting industry. Lorem Ipsum has been the industry's standard dummy text ever</p>
  <svg class="wave" width="295" height="170" viewBox="0 0 295 170" aria-hidden="true"><path d="M0 30 Q147 -20 295 30 V170 H0Z" fill="#4fb848"/></svg>
  <div class="avatar" role="img" aria-label="Portrait of client Ansel"></div>
  <h4>Ansel</h4><small>Client</small>
</div>
<svg class="arrow" style="left:41px" viewBox="0 0 44 44" aria-hidden="true"><circle cx="22" cy="22" r="22" fill="#a9a9a9"/><path d="M25 13 L16 22 L25 31" stroke="#fff" stroke-width="3" fill="none"/></svg>
<svg class="arrow" style="left:1116px" viewBox="0 0 44 44" aria-hidden="true"><circle cx="22" cy="22" r="22" fill="#111"/><path d="M19 13 L28 22 L19 31" stroke="#fff" stroke-width="3" fill="none"/></svg>

<section class="contact-bg"></section>
<h2 class="section-title" style="top:4140px">Contact Us</h2>
<div class="info-item" style="top:4228px">
  <div class="info-icon"><svg width="20" height="20" viewBox="0 0 20 20"><path d="M4 2 L8 2 L9 6 L7 8 Q9 12 12 13 L14 11 L18 12 L18 16 Q10 18 4 10 Q2 6 4 2Z" fill="#4fb848"/></svg></div>
  <div><h5>Call Us</h5><span>(555) 014-2290</span></div>
</div>
<div class="info-item" style="top:4288px">
  <div class="info-icon"><svg width="20" height="16" viewBox="0 0 20 16"><rect x="1" y="1" width="18" height="14" rx="2" fill="#4fb848"/><path d="M1 2 L10 9 L19 2" stroke="#fff" stroke-width="1.6" fill="none"/></svg></div>
  <div><h5>Website</h5><span>www.verdano-ledger.com</span></div>
</div>
<div class="info-item" style="top:4346px">
  <div class="info-icon"><svg width="16" height="22" viewBox="0 0 16 22"><path d="M8 21 Q1 12 1 8 A7 7 0 0 1 15 8 Q15 12 8 21Z" fill="#4fb848"/><circle cx="8" cy="8" r="2.6" fill="#fff"/></svg></div>
  <div><h5>Location</h5><span>P.O. Box 4180<br>Cedar Point, MT 59000</span></div>
</div>
<div class="field" style="left:517px;top:4215px;width:274px;height:43px">First Name</div>
<div class="field" style="left:811px;top:4215px;width:274px;height:43px">Last Name</div>
<div class="field" style="left:517px;top:4275px;width:274px;height:43px">Email Id</div>
<div class="field" style="left:811px;top:4275px;width:274px;height:43px">Phone Number</div>
<div class="field" style="left:517px;top:4337px;width:568px;height:128px">Type Your Message</div>
<a class="btn submit">Submit</a>

<footer class="site-footer">
  <div class="brand"><span class="brand-dot"></span>VERDANO</div>
  <div class="social"><span></span><span></span><span></span></div>
  <div class="foot-col" style="left:360px"><h4>Quick Links</h4>
    <ul><li>Home</li><li>About Us</li><li>Our Services</li><li>Why Choose Us</li><li>Testimonials</li><li>Contact us</li></ul></div>
  <div class="foot-col" style="left:553px"><h4>Contact Info</h4>
    <ul><li>✉ www.verdano-ledger.com</li><li>☏ (555) 014-2290</li><li>⚲ P.O. Box 4180</li><li style="padding-left:24px">Cedar Point, MT 59000</li></ul></div>
  <div class="foot-col" style="left:853px;top:98px"><h4>Sign Up&nbsp; Our<br>Newsletter</h4></div>
  <div class="newsletter">Enter Your Mail Address<i><svg width="64" height="42" viewBox="0 0 64 42"><path d="M22 21 L42 12 L36 31 L31 24Z" fill="none" stroke="#fff" stroke-width="2"/></svg></i></div>
  <div class="foot-rule"></div>
  <div class="copyright">© 2023 VERDANO .All Rights Reserved</div>
</footer>

</body>
</html>
```